Board Presentation template

Design a simple and clean PowerPoint slide templates for a Board meeting. The slides should have predominantly white backgrounds and use the colors of our Logo (attached): Tones of grey and orange and blue.
The company name is called Harbor Crest Gauges.
It sell, calibrate, service and repair industrial and commercial scales of all types. In particular, Truck scales, floor scales, counting scales and benchtop scales.
There is no website for Harbor Crest Gauges, but we have three affiliates that have their own websites:
https://www.fernmoorweigh.com/
https://lantovalegaugeandbalance.com/
https://qtwegh.com/
Target Market(s)
Industrial and Commercial Weighing systems
Industry/Entity Type
Look and feel
Each slider illustrates characteristics of the customer's brand and the style your logo design should communicate.

```html
<!DOCTYPE html>
<html lang="en">
<head>
<meta charset="utf-8">
<title>Harbor Crest Gauges – Board Presentation</title>
<link href="https://fonts.googleapis.com/css2?family=Oswald:wght@500;600;700&family=Lato:wght@400;700&family=Nunito:wght@500;700&family=Montserrat:wght@800&display=swap" rel="stylesheet">
<style>
  :root{
    --accent:#e8772e;
    --dark:#3e464d;
    --blue:#1f4e8c;
    --ink:#2b2b2b;
    --muted:#6b6b6b;
    --backdrop:#a3a3a3;
    --white:#ffffff;
  }
  *{box-sizing:border-box;margin:0;padding:0}
  html,body{width:1033px;height:1200px;overflow:hidden;background:var(--backdrop)}
  .board{position:absolute;left:0;top:0;width:1784px;height:2072px;transform:scale(0.57903);transform-origin:0 0}
  .slide{position:absolute;width:750px;height:422px;background:var(--white);overflow:hidden;font-family:"Lato",sans-serif;color:var(--ink)}
  .col-a{left:84px}.col-b{left:948px}
  .row-1{top:62px}.row-2{top:547px}.row-3{top:1044px}.row-4{top:1559px}
  .abs{position:absolute}

  .slide-title{position:absolute;left:36px;top:22px;font-family:"Oswald",sans-serif;font-weight:600;font-size:23px;color:var(--dark);letter-spacing:.2px}
  .corner-brand{position:absolute;right:36px;top:22px;display:flex;align-items:center;gap:6px;font-family:"Oswald",sans-serif;font-weight:600;font-size:11px;color:var(--blue);line-height:1.1;text-align:right}
  .corner-brand .dot{width:10px;height:10px;border-radius:50%;background:var(--accent)}

  .footer{position:absolute;left:0;bottom:0;width:750px;height:70px}
  .footer svg{position:absolute;left:0;top:0}
  .footer .date{position:absolute;left:37px;bottom:4px;font-size:10px;color:var(--white)}
  .footer .page{position:absolute;right:38px;bottom:6px;font-size:10px;font-weight:700;color:var(--white)}

  .photo{position:absolute}

  /* cover */
  .cover .brand{left:36px;top:112px;font-family:"Oswald",sans-serif;font-weight:600;font-size:25px;color:var(--blue);line-height:1.1;display:flex;align-items:center;gap:10px}
  .cover .brand .dot{width:16px;height:16px;border-radius:50%;background:var(--accent)}
  .cover .headline{left:36px;top:190px;width:345px;font-family:"Oswald",sans-serif;font-weight:500;font-size:25px;line-height:36px;color:var(--dark)}
  .cover .lead{left:37px;top:306px;width:340px;font-size:13.5px;line-height:23px;color:var(--ink)}

  /* contents */
  .toc-band{left:0;top:0;width:70px;height:422px;background:var(--blue)}
  .toc-band span{position:absolute;left:35px;top:211px;transform:translate(-50%,-50%) rotate(-90deg);white-space:nowrap;font-family:"Oswald",sans-serif;font-weight:700;font-size:26px;letter-spacing:2px;color:var(--white)}
  .toc-item{position:absolute;left:358px;display:flex;align-items:center;gap:13px;font-family:"Nunito",sans-serif;font-weight:500;font-size:20px;color:var(--ink)}
  .toc-num{width:44px;height:44px;border-radius:50%;border:3px solid var(--white);box-shadow:0 0 0 1px #ddd;display:flex;align-items:center;justify-content:center;color:var(--white);font-family:"Oswald",sans-serif;font-weight:600;font-size:19px}
  .toc-num.dark{background:var(--dark)}.toc-num.accent{background:var(--accent)}
  .toc-date{left:93px;top:399px;font-size:10px;color:var(--white)}
  .toc-page{right:34px;top:399px;font-size:10px;font-weight:700;color:var(--accent)}

  /* about */
  .about-copy{left:37px;top:70px;width:368px;font-size:13.5px;line-height:29px;text-align:justify;color:#3a3a3a}
  .about-copy p+p{margin-top:29px}

  /* services */
  .services-lead{left:37px;top:70px;width:680px;font-size:12px;line-height:23px;color:#2f2f2f}
  .service{position:absolute;top:148px;width:170px;height:170px;border-radius:50%;background:var(--white);border:14px solid var(--dark);box-shadow:0 4px 8px rgba(0,0,0,.18);text-align:center;padding-top:18px}
  .service.accent{border-color:var(--accent)}
  .service svg{display:block;margin:0 auto 4px}
  .service h3{font-size:11.5px;font-weight:700;color:var(--dark);margin-bottom:6px}
  .service.accent h3{color:var(--accent)}
  .service p{font-size:7.5px;line-height:12px;color:#666;padding:0 6px}

  /* intro */
  .intro-bg{left:0;top:0;width:750px;height:422px}
  .intro-title{left:0;width:760px;top:128px;text-align:center;font-family:"Oswald",sans-serif;font-weight:700;font-size:66px;color:#37393b;letter-spacing:.5px}

  /* graph */
  .stat{position:absolute;left:37px}
  .stat b{display:block;font-family:"Lato",sans-serif;font-weight:400;font-size:30px;line-height:34px;padding-left:15px}
  .stat span{font-size:12px}
  .stat.accent b,.stat.accent span{color:var(--accent)}
  .stat.dark b{color:var(--blue)}
  .graph-side{left:568px;top:95px;width:143px;font-size:11.5px;line-height:19.5px;text-align:justify;color:#2f2f2f}
  .graph-side p+p{margin-top:19.5px}
  .graph-note{left:190px;top:296px;width:340px;font-size:12px;line-height:23px;color:#2f2f2f}

  /* team */
  .member{position:absolute;top:95px;width:151px;height:224px;background:var(--white);box-shadow:0 1px 6px rgba(0,0,0,.16);text-align:center}
  .member .avatar{width:58px;height:58px;border-radius:50%;margin:20px auto 0;background:radial-gradient(circle at 50% 40%,#8a7a6c,#3a3430)}
  .member h4{margin-top:19px;font-family:"Montserrat",sans-serif;font-weight:800;font-size:11px;color:#222;letter-spacing:.3px}
  .member .role{margin-top:6px;font-size:10px;font-weight:700;color:#222}
  .member p{margin-top:6px;font-size:9px;line-height:16px;color:#777;padding:0 8px}
  .member .social{display:flex;justify-content:center;gap:4px;margin-top:7px}
  .member .social i{width:15px;height:15px;border-radius:50%;border:1px solid #ccc;display:block}
  .member .social i:first-child{background:var(--accent);border-color:var(--accent)}

  /* contact */
  .contact-mark{left:345px;top:58px;width:60px;height:60px;border-radius:50%;border:5px solid var(--dark)}
  .contact-brand{left:0;width:750px;top:168px;text-align:center;font-family:"Oswald",sans-serif;font-weight:600;font-size:38px;line-height:44px;color:var(--blue)}
  .contact-item{position:absolute;top:256px;display:flex;gap:10px}
  .contact-item .pin{width:32px;height:32px;border-radius:50%;background:var(--accent);display:flex;align-items:center;justify-content:center;flex:none;margin-top:6px}
  .contact-item h5{font-size:13px;font-weight:700;color:#555;letter-spacing:.3px}
  .contact-item div{font-size:12.5px;line-height:18px;color:#222}
  .contact-item h5+div{margin-top:6px}
  .thanks{left:0;width:770px;top:318px;text-align:center;font-family:"Montserrat",sans-serif;font-weight:800;font-size:37px;color:var(--accent);letter-spacing:.5px}
</style>
</head>
<body>
<div class="board">

  <!-- Slide 1: cover -->
  <section class="slide cover col-a row-1">
    <div class="abs brand"><span class="dot"></span><span>HARBOR CREST<br>GAUGES</span></div>
    <h1 class="abs headline">DRIVING ACCURACY. DELIVERING PERFORMANCE, YOUR TRUSTED PARTNER IN WEIGHING SOLUTIONS.</h1>
    <p class="abs lead">Committed to excellence in industrial and commercial weighing solutions.</p>
    <svg class="abs" style="left:0;top:0" width="750" height="422" viewBox="0 0 750 422">
      <defs>
        <radialGradient id="coverPhoto" cx="55%" cy="55%" r="60%">
          <stop offset="0" stop-color="#e0773a"/>
          <stop offset="0.35" stop-color="#7a3a2a"/>
          <stop offset="1" stop-color="#2a2e36"/>
        </radialGradient>
      </defs>
      <circle cx="636" cy="210" r="230" fill="var(--accent)"/>
      <circle cx="648" cy="210" r="222" fill="url(#coverPhoto)" role="img" aria-label="Laser cutting head over a metal plate with sparks"/>
    </svg>
  </section>

  <!-- Slide 2: contents -->
  <section class="slide col-b row-1">
    <div class="abs toc-band"><span>TABLE OF CONTENT</span></div>
    <div class="photo" style="left:74px;top:0;width:306px;height:422px;background:linear-gradient(160deg,#5b6068 0%,#8a8d92 40%,#c96a3a 70%,#4a4e55 100%)" role="img" aria-label="Technician in hard hat and orange suit servicing industrial pipework"></div>
    <div class="toc-item" style="top:48px"><span class="toc-num dark">I</span>About Harbor Crest Gauges</div>
    <div class="toc-item" style="top:119px"><span class="toc-num accent">II</span>Our Services</div>
    <div class="toc-item" style="top:190px"><span class="toc-num dark">III</span>Why Choose Us</div>
    <div class="toc-item" style="top:262px"><span class="toc-num accent">IV</span>Our Graph</div>
    <div class="toc-item" style="top:333px"><span class="toc-num dark">V</span>Contact Us</div>
    <div class="abs toc-date">25 Oct 2025</div>
    <div class="abs toc-page">Page No: 02</div>
  </section>

  <!-- Slide 3: about -->
  <section class="slide col-a row-2">
    <h2 class="slide-title">ABOUT HARBOR CREST GAUGES</h2>
    <div class="corner-brand"><span class="dot"></span>HARBOR CREST<br>GAUGES</div>
    <div class="abs about-copy">
      <p>Lorem ipsum dolor sit amet, consectetur adipiscing elit, sed do eiusmod tempor incididunt ut labore et dolore magna aliqua. Ut enim ad minim veniam, quis nostrud exercitation ullamco laboris nisi ut aliquip ex ea commodo consequat. Duis aute irure dolor in reprehenderit in voluptate velit esse cillum dolore eu fugiat nulla pariatur.</p>
      <p>Excepteur sint occaecat cupidatat non proident, sunt in im ad minim veniam, quis nostrudim ad minim veniam, quis nostrudculpaollit anim id est laborum.</p>
    </div>
    <svg class="abs" style="left:440px;top:74px" width="274" height="274" viewBox="0 0 274 274">
      <defs>
        <radialGradient id="aboutPhoto" cx="50%" cy="45%" r="60%">
          <stop offset="0" stop-color="#d98a3a"/>
          <stop offset="0.5" stop-color="#6b6e72"/>
          <stop offset="1" stop-color="#2f3b48"/>
        </radialGradient>
      </defs>
      <circle cx="137" cy="137" r="134" fill="none" stroke="var(--dark)" stroke-width="3.5"/>
      <circle cx="137" cy="137" r="112" fill="url(#aboutPhoto)" role="img" aria-label="Two engineers in hard hats and safety vests working on machinery"/>
    </svg>
    <div class="footer">
      <svg width="750" height="70" viewBox="0 0 750 70"><path d="M0 48 C300 46 520 36 750 22 L750 70 L0 70 Z" fill="var(--accent)"/><path d="M750 0 C600 28 420 48 160 70 L750 70 Z" fill="var(--dark)"/></svg>
      <span class="date">25 Oct 2025</span><span class="page">Page No: 03</span>
    </div>
  </section>

  <!-- Slide 4: services -->
  <section class="slide col-b row-2">
    <h2 class="slide-title">OUR SERVICES</h2>
    <div class="corner-brand"><span class="dot"></span>HARBOR CREST<br>GAUGES</div>
    <p class="abs services-lead">Duis aute irure dolor in reprehenderit in voluptate velit esse cillum dolore eu fugiat nulla pariatur. Excepteur sint occaecat cupidatat non proident, sunt in culpa qui officia deserunt mollit anim id est laborum.</p>
    <div class="service" style="left:53px">
      <svg width="26" height="24" viewBox="0 0 26 24"><path d="M3 22V4h6v18M9 8h12v14M13 12h4v6h-4z" fill="none" stroke="var(--dark)" stroke-width="2"/></svg>
      <h3>REPAIR INDUSTRIAL</h3>
      <p>Excepteur sint occaecat cupidatat non proident, sunt in culpa qui officia deserunt mollit anim id est laborum.</p>
    </div>
    <div class="service accent" style="left:209px">
      <svg width="26" height="24" viewBox="0 0 26 24"><circle cx="13" cy="6" r="4" fill="var(--accent)"/><path d="M5 22v-6a8 8 0 0 1 16 0v6z" fill="var(--accent)"/></svg>
      <h3>COMMERCIAL</h3>
      <p>Excepteur sint occaecat cupidatat non proident, sunt in culpa qui officia deserunt mollit anim id est laborum.</p>
    </div>
    <div class="service" style="left:367px">
      <svg width="26" height="24" viewBox="0 0 26 24"><rect x="6" y="2" width="14" height="20" rx="1" fill="none" stroke="var(--dark)" stroke-width="2"/><path d="M9 7h8M9 12h2M13 12h2M9 16h2M13 16h2" stroke="var(--dark)" stroke-width="2"/></svg>
      <h3>ESTIMATING</h3>
      <p>Excepteur sint occaecat cupidatat non proident, sunt in culpa qui officia deserunt mollit anim id est laborum.</p>
    </div>
    <div class="service accent" style="left:524px">
      <svg width="26" height="24" viewBox="0 0 26 24"><path d="M3 22L11 4l4 8 3-4 5 14z" fill="none" stroke="var(--accent)" stroke-width="2"/></svg>
      <h3>ARCHITECTS</h3>
      <p>Excepteur sint occaecat cupidatat non proident, sunt in culpa qui officia deserunt mollit anim id est laborum.</p>
    </div>
    <div class="footer">
      <svg width="750" height="70" viewBox="0 0 750 70"><path d="M0 48 C300 46 520 36 750 22 L750 70 L0 70 Z" fill="var(--accent)"/><path d="M750 0 C600 28 420 48 160 70 L750 70 Z" fill="var(--dark)"/></svg>
      <span class="date">25 Oct 2025</span><span class="page">Page No: 04</span>
    </div>
  </section>

  <!-- Slide 5: introduction -->
  <section class="slide col-a row-3">
    <div class="abs intro-bg" style="background:radial-gradient(ellipse at 65% 70%,#f3e6d8 0%,#e9ebee 40%,#dde1e6 100%)" role="img" aria-label="Faded laser cutter with sparks"></div>
    <div class="corner-brand"><span class="dot"></span>HARBOR CREST<br>GAUGES</div>
    <h2 class="abs intro-title">INTRODUCTION</h2>
    <div class="footer">
      <svg width="750" height="70" viewBox="0 0 750 70"><path d="M0 48 C300 46 520 36 750 22 L750 70 L0 70 Z" fill="var(--accent)"/><path d="M750 0 C600 28 420 48 160 70 L750 70 Z" fill="var(--dark)"/></svg>
      <span class="date">25 Oct 2025</span><span class="page">Page No: 05</span>
    </div>
  </section>

  <!-- Slide 6: graph -->
  <section class="slide col-b row-3">
    <h2 class="slide-title">OUR GRAPH</h2>
    <div class="corner-brand"><span class="dot"></span>HARBOR CREST<br>GAUGES</div>
    <div class="stat accent" style="top:117px"><b>657</b><span>Excepteur sint</span></div>
    <div class="stat dark" style="top:197px"><b>472</b><span>Duis aute iruret</span></div>
    <svg class="abs" style="left:180px;top:90px" width="350" height="190" viewBox="0 0 350 190">
      <line x1="4" y1="168" x2="344" y2="168" stroke="#ddd" stroke-width="1"/>
      <rect x="15" y="83" width="31" height="85" fill="var(--dark)"/>
      <rect x="71" y="54" width="31" height="114" fill="var(--blue)"/>
      <rect x="129" y="118" width="31" height="50" fill="var(--dark)"/>
      <rect x="187" y="109" width="31" height="59" fill="var(--blue)"/>
      <rect x="243" y="52" width="31" height="116" fill="var(--dark)"/>
      <rect x="303" y="9" width="31" height="159" fill="var(--accent)"/>
      <g font-family="Lato, sans-serif" font-size="9" font-weight="700" fill="#333" text-anchor="middle">
        <text x="30" y="183">F1</text><text x="86" y="183">F2</text><text x="145" y="183">F3</text>
        <text x="202" y="183">F4</text><text x="258" y="183">F5</text><text x="318" y="183">F6</text>
      </g>
    </svg>
    <div class="abs graph-side">
      <p>Duis aute irure dolor in reprehenderit in voluptate velit esse cillum dolore eu fugiat nulla pariatur.</p>
      <p>Excepteur sint occaecat cupidatat non proident, sunt in culpa qui officia deserunt mollit anim id est laborum.</p>
    </div>
    <p class="abs graph-note">Excepteur sint occaecat cupidatat non proident, sunt in culpa qui officia deserunt mollit anim id est laborum.</p>
    <div class="footer">
      <svg width="750" height="70" viewBox="0 0 750 70"><path d="M0 48 C300 46 520 36 750 22 L750 70 L0 70 Z" fill="var(--accent)"/><path d="M750 0 C600 28 420 48 160 70 L750 70 Z" fill="var(--dark)"/></svg>
      <span class="date">25 Oct 2025</span><span class="page">Page No: 06</span>
    </div>
  </section>

  <!-- Slide 7: team -->
  <section class="slide col-a row-4">
    <h2 class="slide-title">OUR TEAM</h2>
    <div class="corner-brand"><span class="dot"></span>HARBOR CREST<br>GAUGES</div>
    <div class="member" style="left:38px">
      <div class="avatar" role="img" aria-label="Portrait of Owen Pratt"></div>
      <h4>OWEN PRATT</h4><div class="role">Founder</div>
      <p>Sed ut perspiciatis unde omnis iste natus er ror sit voluptatem accusantium dolorea.</p>
      <div class="social"><i></i><i></i><i></i></div>
    </div>
    <div class="member" style="left:211px">
      <div class="avatar" role="img" aria-label="Portrait of Miles Corder"></div>
      <h4>MILES CORDER</h4><div class="role">Founder</div>
      <p>Itaque earum rerum hic tenetur a sapiente delectus, ut aut reiciendis voluptatibus</p>
      <div class="social"><i></i><i></i><i></i></div>
    </div>
    <div class="member" style="left:385px">
      <div class="avatar" role="img" aria-label="Portrait of Nora Vale"></div>
      <h4>NORA VALE</h4><div class="role">Founder</div>
      <p>Sed ut perspiciatis unde omnis iste natus er ror sit volupta tem accusantium</p>
      <div class="social"><i></i><i></i><i></i></div>
    </div>
    <div class="member" style="left:558px">
      <div class="avatar" role="img" aria-label="Portrait of Miles Corder"></div>
      <h4>MILES CORDER</h4><div class="role">Founder</div>
      <p>Earum rerum hic tenetur a sapiente delectus, ut aut reiciendis voluptatibus</p>
      <div class="social"><i></i><i></i><i></i></div>
    </div>
    <div class="footer">
      <svg width="750" height="70" viewBox="0 0 750 70"><path d="M0 48 C300 46 520 36 750 22 L750 70 L0 70 Z" fill="var(--accent)"/><path d="M750 0 C600 28 420 48 160 70 L750 70 Z" fill="var(--dark)"/></svg>
      <span class="date">25 Oct 2025</span><span class="page">Page No: 07</span>
    </div>
  </section>

  <!-- Slide 8: contact -->
  <section class="slide col-b row-4">
    <h2 class="slide-title">CONTACT US</h2>
    <div class="abs contact-mark"></div>
    <div class="abs contact-brand">HARBOR CREST GAUGES</div>
    <div class="contact-item" style="left:34px">
      <span class="pin"><svg width="14" height="16" viewBox="0 0 14 16"><path d="M7 15S1 9 1 6a6 6 0 0 1 12 0c0 3-6 9-6 9z" fill="#fff"/><circle cx="7" cy="6" r="2" fill="var(--accent)"/></svg></span>
      <div><h5>LOCATION:</h5><div>Harbor Crest Gauges, United States</div></div>
    </div>
    <div class="contact-item" style="left:298px">
      <span class="pin"><svg width="14" height="12" viewBox="0 0 14 12"><rect x="1" y="1" width="12" height="10" rx="1" fill="#fff"/><path d="M1 2l6 5 6-5" fill="none" stroke="var(--accent)" stroke-width="1.5"/></svg></span>
      <div><h5>EMAIL US:</h5><div>info@harborcrestgauges.com</div></div>
    </div>
    <div class="contact-item" style="left:555px">
      <span class="pin"><svg width="14" height="14" viewBox="0 0 14 14"><path d="M3 1l3 3-2 2a8 8 0 0 0 4 4l2-2 3 3-2 2C6 13 1 8 1 3z" fill="#fff"/></svg></span>
      <div><h5>PHONE NUMBER:</h5><div>+1 555 010 2040</div></div>
    </div>
    <div class="abs thanks">THANK YOU</div>
    <div class="footer">
      <svg width="750" height="70" viewBox="0 0 750 70"><path d="M0 48 C300 46 520 36 750 22 L750 70 L0 70 Z" fill="var(--accent)"/><path d="M750 0 C600 28 420 48 160 70 L750 70 Z" fill="var(--dark)"/></svg>
      <span class="date">25 Oct 2025</span><span class="page">Page No: 08</span>
    </div>
  </section>

</div>
</body>
</html>
```